New Business Card Design Project

The idea, the card is to put a card, which contains two companies at the same time. Please see the attached data and idea of how the current cards are.
Updates
VELDAK
Constructora
Ferrotrac Delmar SRL.
Equipos para Plantas de Tratamientos y Acueductos, Alquiler de Equipos Pesados para la Construcción.
C / Pedro Lucena No.47
Loma Clara, Santo Domingo. República Dominicana.
Tel .: 1809 555 4172
CEL: 1829 555 6281
teodoro@ferrotracdelmar.net
veldakobras@mailvista.example
www.ferrotracdelmar.net
Veldak construction.
Es una empresa constructora.
NOTA: La idea es llevar una sola tarjeta para dos compañías. o si no resulta hacer un diseño en cada lado, uno para cada empresa.Equipos para Plantas de Tratamiento y Acueductos, Alquiler de Equipos Pesados para la Construcción.
Deben de llevar, los logos.
VELDAK
Constructora
Ferrotrac Delmar SRL.
C / Pedro Lucena No.47
Tel .: 1809 555 4172
CEL: 1829 555 6281
Veldak construction.
VELDAK
Constructora
Ferrotrac Delmar SRL.
C / Pedro Lucena No.47
Tel .: 1809 555 4172
CEL: 1829 555 6281
Veldak construction.
It is a construction company
NOTE: The idea is to carry a single card for two companies. or if it does not turn out to make a design on each side, one for each company. Equipment for Treatment Plants and Aqueducts, Rental of Heavy Equipment for Construction.
They must carry, the logos.
How is the design similar to that, send example, for data, from previous designs.
What I'm looking for is a new design, not a remodeled copy
ferrotracdelmar
Tel: 1809 555 4172
cel: 1829 555 6281
teodoro@ferrotracdelmar.net
Direccion:
C/ Pedro Lucena # 47
Loma clara, Santo Domingo
Republica Dominicana
Veldak
constructora
Tel: 1809 555-3907
Cel: 1829 555 6281
veldaksa1@mailvista.example
Direccion:
C/ Pedro Lucena # 47
Republica Dominicana
Contact Information for Business Card
FERROTRAC DELMAR, S.R.L.
C/ Tomás Benítez Olarte esquina Pedro Lucena # 47
Loma Clara, Santo Domingo, República Dominicana
Office: 809.555.4172
Fax: 809.555.8364
Cel (Local): 829 555 6281
E-mail: DUMMY@DUMMY.com
E-mail:DUMMY@gmail.com
Website: http://www.DUMMY.com
Look and feel
Each slider illustrates characteristics of the customer's brand and the style your logo design should communicate.

```html
<!DOCTYPE html>
<html lang="es">
<head>
<meta charset="UTF-8">
<title>Veldak Constructora y Ferrotrac Delmar – Tarjeta de presentación</title>
<link href="https://fonts.googleapis.com/css2?family=Josefin+Sans:wght@400;600&family=Montserrat:wght@500;600&family=Roboto+Condensed:wght@700&display=swap" rel="stylesheet">
<style>
  :root {
    --page-bg: #ffffff;
    --card-bg: #ffffff;
    --card-border: #3a3a3a;
    --brand-orange: #e8601e;
    --brand-charcoal: #333333;
    --contact-navy: #26306b;
    --title-grey: #444444;
  }
  * { margin: 0; padding: 0; box-sizing: border-box; }
  html, body {
    width: 802px;
    height: 1200px;
    overflow: hidden;
    background: var(--page-bg);
  }
  .business-card {
    position: absolute;
    left: 21px;
    top: 383px;
    width: 760px;
    height: 433px;
    background: var(--card-bg);
    border: 1px solid var(--card-border);
    overflow: hidden;
  }
  .brands {
    position: absolute;
    left: 34px;
    top: 140px;
    width: 330px;
    display: flex;
    flex-direction: column;
    gap: 30px;
  }
  .brand {
    display: flex;
    align-items: center;
    gap: 12px;
  }
  .brand-mark {
    flex: none;
    background: var(--brand-orange);
  }
  .brand-name {
    font-family: "Roboto Condensed", sans-serif;
    font-weight: 700;
    line-height: 1;
    color: var(--brand-charcoal);
  }
  .brand--primary .brand-mark { width: 52px; height: 52px; }
  .brand--primary .brand-name { font-size: 66px; letter-spacing: -1px; }
  .brand--secondary .brand-mark { width: 22px; height: 22px; }
  .brand--secondary .brand-name { font-size: 28px; letter-spacing: 0.5px; }
  .divider {
    position: absolute;
    left: 386px;
    top: 100px;
    width: 2px;
    height: 247px;
    background: linear-gradient(to bottom, transparent, var(--brand-orange) 15%, var(--brand-orange) 85%, transparent);
  }
  .holder {
    position: absolute;
    left: 439px;
    top: 40px;
  }
  .holder-name {
    font-family: "Josefin Sans", sans-serif;
    font-weight: 600;
    font-size: 26px;
    color: var(--brand-orange);
    letter-spacing: 1px;
  }
  .holder-role {
    font-family: "Josefin Sans", sans-serif;
    font-weight: 400;
    font-size: 20px;
    color: var(--title-grey);
    letter-spacing: 3px;
    margin-top: 2px;
  }
  .contact-list {
    position: absolute;
    left: 439px;
    top: 224px;
    list-style: none;
  }
  .contact-item {
    display: flex;
    align-items: flex-start;
    gap: 18px;
    margin-bottom: 15px;
    font-family: "Montserrat", sans-serif;
    font-weight: 500;
    font-size: 14px;
    line-height: 17px;
    color: var(--contact-navy);
    letter-spacing: 0.8px;
  }
  .contact-icon {
    flex: none;
    width: 17px;
    height: 17px;
  }
  .web-band {
    position: absolute;
    left: 0;
    top: 388px;
    width: 100%;
    height: 33px;
    background: var(--brand-orange);
    font-family: "Montserrat", sans-serif;
    font-weight: 500;
    font-size: 18px;
    letter-spacing: 2px;
    color: #ffffff;
    text-align: center;
    line-height: 33px;
  }
</style>
</head>
<body>
  <section class="business-card">
    <div class="brands">
      <div class="brand brand--primary">
        <span class="brand-mark"></span>
        <span class="brand-name">VELDAK</span>
      </div>
      <div class="brand brand--secondary">
        <span class="brand-mark"></span>
        <span class="brand-name">FERROTRAC DELMAR</span>
      </div>
    </div>

    <div class="divider"></div>

    <header class="holder">
      <h1 class="holder-name">Lic. Teodoro Almánzar</h1>
      <p class="holder-role">President</p>
    </header>

    <ul class="contact-list">
      <li class="contact-item">
        <svg class="contact-icon" viewBox="0 0 20 20" aria-hidden="true">
          <circle cx="10" cy="10" r="8.5" fill="none" stroke="#e8601e" stroke-width="1.5"/>
          <path d="M10 5a3 3 0 0 1 3 3c0 2.3-3 6-3 6s-3-3.7-3-6a3 3 0 0 1 3-3z" fill="#e8601e"/>
          <circle cx="10" cy="8" r="1.1" fill="#fff"/>
        </svg>
        <span>C/ Pedro Lucena #47.<br>Loma Clara, Santo Domingo ,<br>Republica Dominicana.</span>
      </li>
      <li class="contact-item">
        <svg class="contact-icon" viewBox="0 0 20 20" aria-hidden="true">
          <circle cx="10" cy="10" r="8.5" fill="none" stroke="#e8601e" stroke-width="1.5"/>
          <path d="M7 5.5l1.6 2.2-1 1.1a6 6 0 0 0 3.1 3.1l1.1-1 2.2 1.6-1 1.6c-3.8.2-7.6-3.6-7.4-7.4z" fill="#e8601e"/>
        </svg>
        <span>Tel: 809 555 4172.<br>Cel. 829 555 6281.</span>
      </li>
      <li class="contact-item">
        <svg class="contact-icon" viewBox="0 0 20 20" aria-hidden="true">
          <circle cx="10" cy="10" r="8.5" fill="none" stroke="#e8601e" stroke-width="1.5"/>
          <rect x="5.5" y="7" width="9" height="6" fill="#e8601e"/>
          <path d="M5.5 7l4.5 3.5L14.5 7" fill="none" stroke="#fff" stroke-width="1"/>
        </svg>
        <span>teodoro@ferrotracdelmar.net</span>
      </li>
    </ul>

    <footer class="web-band">www.DUMMY.com</footer>
  </section>
</body>
</html>
```